QRV Stationery Design Project

Dear Designers,
We need a new stationery design for company to match our new logo.
Designers should provide a design for the following:
1. Business Card: 3.5x2 Inches.
2. Letterhead: A4 size.
3. Envelops: 25x35.5 Cm.
You can keep the Arabic name at the bottom of the logo Or you can use the separate attached Arabic Name.
Please refer to the attached logo guide for design information.
Sample Business Card information:
Name: Tariq Nawaf
Position: Operation Manager
Tel: +966 920007714 Ex. 500
Fax: +966 (3)8842617
Mob: +966 (5)00387251
email: tariq@qrv-example.com.sa
URL: www.qrv-example.com.sa
Address:
Al Wadi Tower, Suite 303
Nasser bin Salem Str.
Khobar, 31847
Saudi Arabia
Updates
Dear All,
Please note, we had uploaded our logo along with Arabic writing in Adobe illustrator format (.ai).
Regards,
Khalid
Dear All,
A sample data for the business card had been added as per your request.
Regards,
Khalid

```html
<!DOCTYPE html>
<html lang="en">
<head>
<meta charset="utf-8">
<title>QRV Route Systems – Business Card</title>
<link rel="stylesheet" href="https://fonts.googleapis.com/css2?family=Exo+2:wght@400;500;700&display=swap">
<style>
  :root {
    --navy: #0f3458;
    --navy-light: #1d4a72;
    --frame-grey: #7f7f7f;
    --text-grey: #7c7c7c;
    --paper: #ffffff;
    --sheet: #ffffff;
    --sheet-edge: #d9d9d9;
  }
  * { margin: 0; padding: 0; box-sizing: border-box; }
  html, body { width: 1200px; height: 1200px; overflow: hidden; }
  body {
    background: var(--sheet);
    font-family: "Exo 2", "Helvetica Neue", Arial, sans-serif;
    position: relative;
  }
  .sheet {
    position: absolute; inset: 0;
    border: 2px solid var(--sheet-edge);
  }
  .side-label {
    position: absolute; left: 286px;
    font-size: 20px; letter-spacing: 1px; color: #222;
  }
  .side-label--front { top: 68px; }
  .side-label--back { top: 626px; }

  /* Front */
  .card-front {
    position: absolute; left: 248px; top: 144px;
    width: 708px; height: 400px;
    background: var(--frame-grey);
    border-radius: 44px 44px 0 44px;
    padding: 20px;
  }
  .card-front__face {
    position: relative; width: 100%; height: 100%;
    background: var(--paper);
    border-radius: 32px 32px 0 32px;
    overflow: hidden;
  }
  .brand {
    position: absolute; right: 34px; top: 58px;
    display: flex; align-items: center; gap: 10px;
    max-width: 300px;
  }
  .brand__dot {
    flex: none;
    width: 18px; height: 18px; border-radius: 50%;
    background: var(--navy);
  }
  .brand__name {
    font-size: 25px; font-weight: 700; color: var(--navy);
    line-height: 30px;
    white-space: nowrap;
  }
  .person { position: absolute; left: 44px; top: 160px; }
  .person__name { font-size: 27px; color: var(--navy); line-height: 34px; }
  .person__role { font-size: 22px; color: var(--text-grey); line-height: 30px; }
  .contact { position: absolute; left: 44px; top: 262px; }
  .contact p { font-size: 22px; color: var(--text-grey); line-height: 38px; }

  /* Back */
  .card-back {
    position: absolute; left: 248px; top: 700px;
    width: 708px; height: 404px;
    background: var(--navy);
    border-radius: 0 44px 44px 0;
    overflow: hidden;
  }
  .decor {
    position: absolute;
    background: linear-gradient(135deg, var(--navy-light), var(--navy));
    opacity: .85;
  }
  .decor--satellite {
    left: 28px; top: 30px; width: 196px; height: 110px;
    border-radius: 50px;
  }
  .decor--vehicle {
    left: 272px; top: 240px; width: 436px; height: 164px;
    border-radius: 120px 0 0 0;
    background: linear-gradient(160deg, var(--navy-light), var(--navy) 80%);
  }
  .address {
    position: absolute; left: 38px; top: 170px;
    color: var(--paper); font-size: 17px; line-height: 23px;
  }
  .address__block + .address__block { margin-top: 18px; }
</style>
</head>
<body>
  <div class="sheet">
    <div class="side-label side-label--front">FRONT</div>

    <section class="card-front">
      <div class="card-front__face">
        <div class="brand">
          <span class="brand__dot"></span>
          <span class="brand__name">QRV Route Systems</span>
        </div>
        <div class="person">
          <p class="person__name">Mr Name Surname</p>
          <p class="person__role">Managing Director</p>
        </div>
        <div class="contact">
          <p>Mobile: 07000 318274</p>
          <p>Email: name@qrvroutes.com</p>
        </div>
      </div>
    </section>

    <div class="side-label side-label--back">BACK</div>

    <section class="card-back">
      <div class="decor decor--satellite" role="img" aria-label="Faint satellite illustration with signal waves"></div>
      <div class="decor decor--vehicle" role="img" aria-label="Faint tracking truck illustration with signal mast"></div>
      <div class="address">
        <div class="address__block">
          <p>QRV Route Systems</p>
          <p>Main Building 1, Any Warehouse,</p>
          <p>On Industrial Estate,&nbsp; Any Town,</p>
          <p>ZZ9 4QR</p>
        </div>
        <div class="address__block">
          <p>Tel: 0054 9876 20413</p>
          <p>Fax: 0054 9876 20413</p>
          <p>Email: sales@qrvroutes.com</p>
          <p>www.qrvroutes.com</p>
        </div>
      </div>
    </section>
  </div>
</body>
</html>
```